Bramblewood Lodging letterhead

We need a letterhead designed that includes the new logo that has just been designed for our business. The letterhead will need to be formatted for digital use as well as for print.

Target Market(s)

Private tenant, corporate tenants, real estate agents

Industry/Entity Type

Digital

Requirements
Must have
• ABN 87 592 104 316
PO Box 7816, Tilbury Mail Centre QLD 4792
Email: dorian.platt@quillmail.net
Ph: 0438 172 964

```html
<!DOCTYPE html>
<html lang="en">
<head>
<meta charset="utf-8">
<title>Bramblewood Lodging Letterhead</title>
<link href="https://fonts.googleapis.com/css2?family=Arimo:wght@400;700&display=swap" rel="stylesheet">
<style>
  :root {
    --maroon: #5a0020;
    --rust: #7a2b25;
    --label-red: #a3322c;
    --ink: #1a1a1a;
    --paper: #ffffff;
  }
  html, body {
    margin: 0;
    padding: 0;
    overflow: hidden;
    background: var(--paper);
  }
  .letterhead {
    position: relative;
    width: 928px;
    height: 1200px;
    background: var(--paper);
    overflow: hidden;
    font-family: "Arimo", Arial, sans-serif;
    color: var(--ink);
  }
  .band {
    position: absolute;
    left: 0;
    width: 928px;
  }
  .band-top { top: 0; height: 30px; }
  .band-bottom { bottom: 0; height: 40px; }
  .brand {
    position: absolute;
    top: 42px;
    left: 0;
    width: 928px;
    display: flex;
    justify-content: center;
    align-items: center;
    gap: 14px;
  }
  .brand-mark {
    width: 78px;
    height: 80px;
    background: var(--maroon);
    border-radius: 10px;
  }
  .brand-name {
    font-weight: 700;
    color: var(--rust);
    text-transform: uppercase;
    line-height: 1;
  }
  .brand-name .line-1 { display: block; font-size: 40px; letter-spacing: 0.5px; }
  .brand-name .line-2 { display: block; font-size: 19px; margin-top: 6px; letter-spacing: 0.3px; }
  .contact-bar {
    position: absolute;
    top: 1134px;
    left: 0;
    width: 928px;
    display: flex;
    justify-content: center;
    align-items: center;
    gap: 24px;
    font-size: 13px;
  }
  .contact-item {
    display: flex;
    align-items: center;
    gap: 6px;
    white-space: nowrap;
  }
  .contact-item svg { flex: none; }
  .abn-label { color: var(--label-red); }
  .website {
    position: absolute;
    bottom: 12px;
    left: 0;
    width: 928px;
    text-align: center;
    color: var(--paper);
    font-size: 14px;
  }
</style>
</head>
<body>
<div class="letterhead">
  <svg class="band band-top" viewBox="0 0 928 30" aria-hidden="true">
    <path d="M54 0 Q464 54 874 0 Z" fill="var(--maroon)"/>
  </svg>

  <header class="brand">
    <div class="brand-mark"></div>
    <div class="brand-name">
      <span class="line-1">Bramblewood</span>
      <span class="line-2">Lodging</span>
    </div>
  </header>

  <footer>
    <div class="contact-bar">
      <span class="contact-item">
        <svg width="13" height="17" viewBox="0 0 13 17" aria-hidden="true">
          <path d="M6.5 0C2.9 0 0 2.8 0 6.3 0 10.8 6.5 17 6.5 17S13 10.8 13 6.3C13 2.8 10.1 0 6.5 0Z" fill="var(--rust)"/>
          <circle cx="6.5" cy="6.3" r="2.4" fill="var(--paper)"/>
        </svg>
        PO Box 7816, Tilbury Mail Centre QLD 4792
      </span>
      <span class="contact-item">
        <svg width="20" height="15" viewBox="0 0 20 15" aria-hidden="true">
          <path d="M0 6 L10 0 L20 6 V15 H0 Z" fill="var(--rust)"/>
          <path d="M1.5 6.5 L10 11.5 L18.5 6.5" stroke="var(--paper)" stroke-width="1.4" fill="none"/>
        </svg>
        dorian.platt@quillmail.net
      </span>
      <span class="contact-item">
        <svg width="20" height="20" viewBox="0 0 20 20" aria-hidden="true">
          <circle cx="10" cy="10" r="9" fill="none" stroke="var(--rust)" stroke-width="1.5"/>
          <path d="M6.3 5.2 L8 5 L9 7.6 L8 8.6 Q9 10.8 11.4 12 L12.4 11 L15 12 L14.8 13.7 Q13.5 15 11.6 14.4 Q6.8 12.6 5.6 8.4 Q5.2 6.4 6.3 5.2 Z" fill="var(--rust)"/>
        </svg>
        0438 172 964
      </span>
      <span class="contact-item">
        <span class="abn-label">ABN :</span> 87 592 104 316
      </span>
    </div>
    <svg class="band band-bottom" viewBox="0 0 928 40" aria-hidden="true">
      <path d="M54 40 Q464 -34 874 40 Z" fill="var(--rust)"/>
    </svg>
    <div class="website">www.bramblewoodlodging.com</div>
  </footer>
</div>
</body>
</html>
```